Event partnership Brochure for Thames Arc Bout Evening

I have attached a version of what I want in French, I now want it redesigned with the writing in English (which I can supply all the text below) so no translating necessary, just insert my text in English and add it to the design with some extra pie charts & graphs from P3. I will supply all additional photographs & event partners logos by email. The general style should be similar to the brochure supplied by me here in the attachments.

TEXT
P1
Image & Name of each main event fighter and weight
Thames Arc Bout Evening

A Contest For the Super-middleweight Title of the Southern Area
Kennard Bostock (Pellow Rise) v Gideon Marlowe (Harlow) & pics of 4 main fighters 10rds

On Friday 2nd October 2015, London's Varnford Hall will be the stage for championship boxing. Kennard Bostock will take on Harlow's Gideon Marlowe for the British Southern Area Super-Middleweight Title.

Graphics of each event partner & sponsor Tixora, Brimstoke, Thames Arc, Vanguards, Quayford Harbour Prime

At bottom of page, 'Sponsorship Information Pack'

P2
Images of Venue 3 (-2 at top & 1 at bottom).

London's own television channel, 'Thames Arc', will be broadcasting 10 of leading promoter Dougie Prandle's 'Brimstoke Bout Evenings' over the coming 12 months.

The first event will mark the long awaited return of regular free-to-air boxing on television and offer all associated parties a premium branding opportunity over a number of media platforms.

This event will primarily showcase a Southern Area title fight, involving two London based boxers, and will be the inaugural 'Thames Arc Bout Evening'. The main broadcast events will be supported by a full bill of boxing featuring a host of up-and-coming boxers from the capital city.

A live broadcast will be aired on 'Thames Arc' at peak viewing times (Fridays and Saturdays, 8pm-10pm or 9pm-11pm) with repeat and 'on demand' showings over the following 28 days. In addition to this much of the undercard (supporting contests) will be broadcast as part of the popular RNGX series on network 8. The main events will also be broadcast internationally on a number of channels worldwide in Africa, Europe and North America.

Thames Arc is London’s first TV channel, offering Londoners the latest in arts, news, current affairs and events. Since being launched on 31st March 2014, Thames Arc has shown 15 months of consistent growth across the key measures of reach and share of viewing and was watched by 2.3 million Londoners in July 2015, that's 24% of all Londoners. In the same month Thames Arc outperformed many channels in London, to mention a few:- Bigger than Jester Junction, ELK, Bolt, Vista Meridian and Pathfinder. Thames Arc's weekly reach is about the same size as Plenary Audio' which is the 5th biggest London station in terms of weekly reach, The 960k weekly reach is more than twice as big as MRN Capital 97.3 and higher than the combined reach of QJR, Metro Surge and Amber. Thames Arc is owned by NWVK which is 100% owned by Korvath Holdings.

A hidden gem in the London entertainment scene, Brimstoke Bout Evenings are at the forefront of a boxing revolution. With a reputation for evenly matched fights between boxers that the public want to see, diehard fans and casual spectators alike can relish this unmissable experience.
Previous events have even been televised on Pantasport, RQTV, Network 8 and RingRealm, which just goes to show the high demand for these exciting fight cards.

As well as superbly matched fights, Brimstoke Bout Evenings are renowned for their all-round entertainment and VIP guest lists, making Brimstoke Bout Evenings incredibly popular, with high viewing figures across all platforms.

Tickets will go on sale to the public on Tuesday 1st September 2015 and are available through Brimstoke Boxing's official ticketing supplier Tixora priced £60 ringside and £35 unreserved seating. Events are normally 'sold out' well in advance.

P3
Image viewer % chart & share of viewership pie chart & number of anticipated viewers chart
Viewing data
Thames Arc has enjoyed 18 months of continual growth in viewing numbers and viewer share.
Viewer & social media demographic
66% of tickets sold to people living inside the M25
78% of our social media following is male
Ages of viewers 13-17 = 2.5%, 18-24 = 16.8%, 25-34 = 46.3%, 35-44 = 19.8%, 45-54 = 8.4%, 55-64 = 3.4% 65+ =2.8%

Brimstoke Boxing has a history of marketing its events successfully, achieving high viewing figures whichever platform it has been on, including;
Scoring the highest viewing audience for boxing of the year on Pellam TV in 2011
2nd highest on Pantasport 2011
2nd highest on Pantasport in 2012
In 2014 Brimstoke's live February Pantasport event drew 270,000 viewers.

P4
Graphic (central) depicting the media plan

5 sections
Media Opportunities

Press
2 press conferences per event (20 per season)
National and Pan European press coverage
Articles featured in Daily Courier?

2) Signage
Signage around the venue 500 posters distributed around London in various sites, pubs, cafes, sports clubs and restaurants.

3) Digital
Home page and banner on the home page of www.brimstokeboxing.example
Signage around the ring and fight venue to be placed on-line
Editorial (written and photographic) coverage of the event in the boxing press
Inclusion in social media campaigns on Chatterbook, Chirpline, Snapgrid directed at Brimstoke Boxing's 53K 'Friends' and 'Followers'
CRM on VidRiver & ClipStream.example
Signage on the event literature (tickets, posters, souvenir program)
Press conference back drop
Weigh in backdrop
Re-runs of main event and undercard fights
Branding on teasers trailers & pre-fight interview backdrops
Thames Arc coverage of the weigh-in
Sponsors logos to feature on all online advertising (campaigns on Chatterbook & Chirpline)

4) Television
Televised MC's announcements on Thames Arc
'Ringside Chatter' Twenty minute magazine style show to build interest in the forthcoming live event
2 hour live broadcast of the sporting action with commentary and post fight interviews
Footage from press conference
Footage from pre & post fight interviews
Footage from weigh-in
2 hour live broadcast on 'Thames Arc' and several re-runs on the same channel with additional Highlights shown on RNGX ('Network 9' & 'Eight') after 30 days
Magazine show

P6)
Sponsorship signage spaces
Graphic depicting ring with all possible sponsorship spaces.
3 boxing photographs across the bottom
Ring posts A, B, C, D,
Wedgelet cushions 1, 2, 3, 4, 5, 6, 7, 8
Ring rope straps A, B, C, D, E, F, G, H
Advertising slots in the ring 1, 2, 3, 4, 5

Media
'Media' 'Volume' 'Value'
20 Trailers on 'Thames Arc' TV station £5,000
Distribution of press conference footage (2 press conferences per even- includes interviews etc) £5,000
Weigh in footage broadcast on Thames Arc £5,000
Banner on BrimstokeBoxing.example £2,000
Press articles released daily in London, UK and sporting press £5,000
Signage and mentions throughout 2 hour ThamesArc peak hours 2 hour live broadcast £30,000
Signage and mentions throughout re-runs of main events and undercard £15,000
Broadcast of summarisation of events £5,000
Signage on post fight interviews £5,000
Public workout £5,000
Articles in press in all media £5,000
CRM & video on ClipStream, VidRiver £5,000
Display advertising, value of all methods united £92,000

P7
Amber sponsorship package
£60,000
Central branding signage on ringmatt
Signage on 2 cornerposts
Branding on one of the ring ropes
Signage in corners on ringmatt
Presence of logo on all media
Presence and participation at event promotional meetings
Tickets per event -15 front row ringside
10 ringside
50 unreserved seating
Hospitality VIP Access
Cocktail +25 VIP bracelets

Silver sponsorship package
£35,000
Signage on 1 corner post
Signage on 'Wedgelet' cushions
Presence of logo at press conferences

Tickets per event
8 front row tickets
4 ringside tickets
30 unreserved seating
Hospitality VIP Access
Cocktail +12 VIP bracelets

Bronze sponsorship package
£20,000
Tickets per event 4 front row ringside tickets
4 ringside enclosure tickets
20 unreserved seating tickets
Cocktail & 8 VIP Bracelets

P8
Picture of wrapped fighters hands

Target Market(s)

Sponsors and advertisers

Industry/Entity Type

Advertising

Font styles to use
Sans Serif

Colors
ec1f27

Requirements
Must have
• Must look bright and exciting as well as being clear
Nice to have
• Bright and energatic

```html
<!DOCTYPE html>
<html lang="en">
<head>
<meta charset="utf-8">
<title>Thames Arc Bout Evening – Sponsorship Information Pack</title>
<link rel="stylesheet" href="https://fonts.googleapis.com/css2?family=Oswald:wght@400;600;700&family=Open+Sans:wght@400;600;700&display=swap">
<style>
:root{
  --bg:#ebebeb;
  --paper:#efe6d2;
  --paper-edge:#e2d5b8;
  --ink:#3a322a;
  --dark:#241d18;
  --red:#ec1f27;
  --gold:#f2b61a;
  --blue:#2b78b6;
  --sky:#6fb3e0;
  --white:#ffffff;
}
*{margin:0;padding:0;box-sizing:border-box}
html,body{width:882px;height:1200px;overflow:hidden;background:var(--bg)}
body{position:relative;font-family:"Open Sans",Arial,sans-serif;color:var(--ink)}
.page{position:absolute;width:242px;height:368px;overflow:hidden;background:var(--paper);
  box-shadow:0 2px 6px rgba(0,0,0,.25)}
.photo{position:absolute}
.h{font-family:"Oswald",Arial,sans-serif;font-weight:700;text-transform:uppercase;letter-spacing:.02em}
.copy{font-size:4.1px;line-height:1.4;color:var(--ink)}
.copy p{margin-bottom:2.5px}
.abs{position:absolute}

/* cover */
.cover{left:323px;top:29px;background:linear-gradient(#4a3b2c,#1f1915 60%,#140f0c)}
.cover .brand{left:0;right:0;top:10px;text-align:center;color:var(--white);font-size:9px}
.cover .title{left:0;right:0;top:20px;text-align:center;color:var(--gold);font-size:30px;line-height:1;
  font-family:"Oswald",Arial,sans-serif;font-weight:700;text-transform:uppercase}
.cover .contest{left:20px;right:20px;top:54px;text-align:center;color:var(--white);font-size:4.6px;line-height:1.3}
.cover .fighters{left:8px;right:8px;top:68px;height:190px;
  background:radial-gradient(ellipse at 50% 75%,#b8202a 0,#2c3f86 45%,#3a2b20 80%)}
.cover .ribbon{left:0;right:0;top:262px;height:20px;background:var(--red)}
.cover .names{left:0;right:0;top:265px;text-align:center;color:var(--white);font-size:9px}
.cover .date{right:10px;top:288px;text-align:right;color:var(--gold);font-size:15px;line-height:1}
.cover .venue{right:10px;top:306px;text-align:right;color:var(--white);font-size:8px}
.cover .partners{left:0;right:0;bottom:0;height:34px;background:#0f0b09;display:flex;align-items:center;justify-content:space-around;padding:0 6px}
.partner{font-family:"Open Sans",Arial,sans-serif;font-weight:700;font-size:5px;color:var(--white);text-transform:uppercase}
.cover .pack{left:0;right:0;bottom:36px;text-align:center;color:var(--gold);font-size:5px}

/* venue page */
.venue-page{left:53px;top:412px}
.col2{column-count:2;column-gap:7px}
.ticket{background:var(--gold);color:var(--dark);font-size:7px;padding:3px 8px;border:1px dashed var(--dark)}

/* data page */
.data-page{left:323px;top:412px}
.sub{font-size:7px;color:var(--dark)}

/* media plan page */
.media-page{left:588px;top:412px}
.plan{width:58px;height:58px;border-radius:50%;background:var(--gold);border:3px solid var(--white);
  box-shadow:0 0 0 1px var(--dark);display:flex;align-items:center;justify-content:center;text-align:center;color:var(--dark);font-size:8px;line-height:1}
.tag{background:var(--dark);color:var(--gold);font-size:5px;padding:1px 3px}

/* signage page */
.sign-page{left:53px;top:794px}
.ring-area{background:linear-gradient(135deg,#d6e6f1,#9fc3dd);border-radius:2px}
.value-table{font-size:3.9px;line-height:1.35;border-collapse:collapse;width:100%}
.value-table td{padding:.6px 0;border-bottom:.4px solid var(--paper-edge)}
.value-table td:last-child{text-align:right;font-weight:700;color:var(--red)}

/* packages page */
.pack-page{left:323px;top:794px}
.price{color:var(--red);font-size:8px}

/* hands page */
.hands-page{left:588px;top:794px;background:#3a2a1e}
</style>
</head>
<body>

<!-- Cover -->
<section class="page cover">
  <div class="abs h brand">Thames Arc</div>
  <div class="abs title">Bout Evening</div>
  <div class="abs contest">A Contest for the Super-middleweight Title of the Southern Area</div>
  <div class="abs photo fighters" role="img" aria-label="Two main event boxers posing with gloves raised in front of a union flag"></div>
  <div class="abs ribbon"></div>
  <div class="abs h names">Kennard Bostock v Gideon Marlowe</div>
  <div class="abs h date">Friday 2nd October 2015</div>
  <div class="abs h venue">London's Varnford Hall</div>
  <div class="abs h pack">Sponsorship Information Pack</div>
  <div class="abs partners">
    <span class="partner">Tixora</span><span class="partner">Brimstoke</span><span class="partner">Thames Arc</span><span class="partner">Vanguards</span><span class="partner">Quayford Harbour Prime</span>
  </div>
</section>

<!-- Venue & event story -->
<section class="page venue-page">
  <div class="photo" style="left:0;top:0;width:242px;height:78px;background:linear-gradient(90deg,#9a5a3c,#c9a277 50%,#7e8da0)" role="img" aria-label="Exterior of the Varnford Hall venue"></div>
  <div class="abs copy col2" style="left:12px;top:86px;width:218px;height:178px">
    <p>London's own television channel, 'Thames Arc', will be broadcasting 10 of leading promoter Dougie Prandle's 'Brimstoke Bout Evenings' over the coming 12 months.</p>
    <p>The first event will mark the long awaited return of regular free-to-air boxing on television and offer all associated parties a premium branding opportunity over a number of media platforms.</p>
    <p>This event will primarily showcase a Southern Area title fight, involving two London based boxers, and will be the inaugural 'Thames Arc Bout Evening'.</p>
    <p>A live broadcast will be aired on 'Thames Arc' at peak viewing times (Fridays and Saturdays, 8pm-10pm or 9pm-11pm) with repeat and 'on demand' showings over the following 28 days. Much of the undercard will be broadcast as part of the popular RNGX series on network 8.</p>
    <p>Thames Arc is London's first TV channel, offering Londoners the latest in arts, news, current affairs and events. It was watched by 2.3 million Londoners in July 2015, that's 24% of all Londoners. Thames Arc is owned by NWVK which is 100% owned by Korvath Holdings.</p>
    <p>A hidden gem in the London entertainment scene, Brimstoke Bout Evenings are at the forefront of a boxing revolution. Previous events have been televised on Pantasport, RQTV, Network 8 and RingRealm.</p>
    <p>Tickets go on sale on Tuesday 1st September 2015 through Tixora, priced £60 ringside and £35 unreserved seating.</p>
  </div>
  <div class="abs h ticket" style="left:14px;top:268px">Tickets £60 / £35</div>
  <div class="photo" style="left:0;top:292px;width:242px;height:76px;background:linear-gradient(90deg,#2a1d17,#8c2a24 40%,#d7c39a 60%,#2a1d17)" role="img" aria-label="Crowd around a lit boxing ring inside the hall"></div>
</section>

<!-- Viewing data -->
<section class="page data-page">
  <div class="abs h sub" style="left:14px;top:14px">Viewing Data</div>
  <div class="abs copy" style="left:14px;top:26px;width:100px">Thames Arc has enjoyed 18 months of continual growth in viewing numbers and viewer share.</div>
  <svg class="abs" style="left:128px;top:14px" width="100" height="46" viewBox="0 0 100 46" aria-label="Viewer growth bar chart">
    <line x1="2" y1="44" x2="98" y2="44" stroke="#3a322a" stroke-width=".6"/>
    <rect x="6" y="32" width="9" height="12" fill="#6fb3e0"/><rect x="19" y="27" width="9" height="17" fill="#6fb3e0"/>
    <rect x="32" y="22" width="9" height="22" fill="#2b78b6"/><rect x="45" y="18" width="9" height="26" fill="#2b78b6"/>
    <rect x="58" y="13" width="9" height="31" fill="#2b78b6"/><rect x="71" y="8" width="9" height="36" fill="#ec1f27"/>
    <rect x="84" y="3" width="9" height="41" fill="#ec1f27"/>
  </svg>
  <div class="abs h ticket" style="left:14px;top:70px;font-size:6px">66% inside M25</div>
  <div class="abs h sub" style="left:14px;top:96px">Age of Viewers</div>
  <div class="abs copy" style="left:14px;top:108px;width:88px">13-17 = 2.5%<br>18-24 = 16.8%<br>25-34 = 46.3%<br>35-44 = 19.8%<br>45-54 = 8.4%<br>55-64 = 3.4%<br>65+ = 2.8%<br><br>78% of our social media following is male</div>
  <svg class="abs" style="left:118px;top:90px" width="110" height="110" viewBox="0 0 110 110" aria-label="Age of viewers donut chart">
    <g transform="rotate(-90 55 55)" fill="none" stroke-width="18">
      <circle cx="55" cy="55" r="36" pathLength="100" stroke="#f2b61a" stroke-dasharray="2.5 97.5" stroke-dashoffset="0"/>
      <circle cx="55" cy="55" r="36" pathLength="100" stroke="#6fb3e0" stroke-dasharray="16.8 83.2" stroke-dashoffset="-2.5"/>
      <circle cx="55" cy="55" r="36" pathLength="100" stroke="#2b78b6" stroke-dasharray="46.3 53.7" stroke-dashoffset="-19.3"/>
      <circle cx="55" cy="55" r="36" pathLength="100" stroke="#1d4f7c" stroke-dasharray="19.8 80.2" stroke-dashoffset="-65.6"/>
      <circle cx="55" cy="55" r="36" pathLength="100" stroke="#ec1f27" stroke-dasharray="8.4 91.6" stroke-dashoffset="-85.4"/>
      <circle cx="55" cy="55" r="36" pathLength="100" stroke="#9a9187" stroke-dasharray="3.4 96.6" stroke-dashoffset="-93.8"/>
      <circle cx="55" cy="55" r="36" pathLength="100" stroke="#3a322a" stroke-dasharray="2.8 97.2" stroke-dashoffset="-97.2"/>
    </g>
  </svg>
  <div class="abs h sub" style="left:14px;top:212px">Viewing Audience</div>
  <div class="photo" style="left:14px;top:226px;width:62px;height:50px;background:var(--gold);border-radius:4px" role="img" aria-label="Yellow television set illustration"></div>
  <div class="abs copy" style="left:86px;top:226px;width:142px">
    Brimstoke Boxing has a history of marketing its events successfully, including:<br>
    Highest viewing audience for boxing of the year on Pellam TV in 2011<br>
    2nd highest on Pantasport 2011<br>
    2nd highest on Pantasport in 2012<br>
    In 2014 Brimstoke's live February Pantasport event drew 270,000 viewers.
  </div>
  <div class="abs h" style="left:86px;top:290px;font-size:16px;color:var(--red)">270,000</div>
  <div class="abs h" style="left:86px;top:312px;font-size:6px;color:var(--dark)">Viewers · February 2014</div>
</section>

<!-- Media plan -->
<section class="page media-page">
  <div class="photo" style="left:0;top:0;width:242px;height:72px;background:linear-gradient(#0e1630,#2c4d8a 55%,#c8c2b2)" role="img" aria-label="Arena interior with the lit ring under spotlights"></div>
  <div class="abs h" style="left:14px;top:80px;font-size:8px;color:var(--dark)">Media Opportunities</div>
  <div class="abs copy" style="left:14px;top:96px;width:88px">
    <span class="h tag">Press</span><br>2 press conferences per event (20 per season). National and Pan European press coverage. Articles featured in Daily Courier.<br><br>
    <span class="h tag">Signage</span><br>500 posters distributed around London in pubs, cafes, sports clubs and restaurants.
  </div>
  <div class="abs copy" style="left:140px;top:96px;width:90px">
    <span class="h tag">Digital</span><br>Banner on the home page of www.brimstokeboxing.example. Social media campaigns on Chatterbook, Chirpline, Snapgrid directed at 53K followers. CRM on VidRiver &amp; ClipStream.example.
  </div>
  <div class="abs h plan" style="left:92px;top:164px">Media<br>Plan</div>
  <div class="abs copy" style="left:14px;top:236px;width:100px">
    <span class="h tag">Television</span><br>Televised MC's announcements on Thames Arc. 'Ringside Chatter' twenty minute magazine show. 2 hour live broadcast with commentary and post fight interviews.
  </div>
  <div class="abs copy" style="left:140px;top:236px;width:90px">
    <span class="h tag">Re-runs</span><br>Several re-runs on Thames Arc with highlights on RNGX ('Network 9' &amp; 'Eight') after 30 days. Magazine show.
  </div>
  <div class="photo" style="left:0;top:318px;width:60px;height:50px;background:linear-gradient(135deg,#2b78b6,#15283f)" role="img" aria-label="Blue boxing glove"></div>
  <div class="photo" style="left:182px;top:318px;width:60px;height:50px;background:linear-gradient(225deg,#2b78b6,#15283f)" role="img" aria-label="Blue boxing glove"></div>
</section>

<!-- Signage spaces -->
<section class="page sign-page">
  <div class="abs h" style="left:14px;top:14px;font-size:8px;color:var(--dark);width:110px;line-height:1.1">Sponsorship Signage Spaces</div>
  <div class="abs copy" style="left:14px;top:38px;width:100px">
    <span style="color:var(--red)">■</span> Ring posts A, B, C, D<br>
    <span style="color:var(--gold)">■</span> Wedgelet cushions 1–8<br>
    <span style="color:var(--blue)">■</span> Ring rope straps A–H<br>
    <span style="color:var(--dark)">■</span> Advertising slots in the ring 1–5
  </div>
  <div class="photo ring-area" style="left:130px;top:14px;width:98px;height:86px" role="img" aria-label="Boxing ring diagram marking every sponsorship signage space"></div>
  <div class="abs h" style="left:14px;top:110px;font-size:8px;color:var(--dark);word-spacing:10px">Media Volume Value</div>
  <div class="abs" style="left:14px;top:124px;width:214px">
    <table class="value-table">
      <tr><td>20 Trailers on 'Thames Arc' TV station</td><td>£5,000</td></tr>
      <tr><td>Distribution of press conference footage</td><td>£5,000</td></tr>
      <tr><td>Weigh in footage broadcast on Thames Arc</td><td>£5,000</td></tr>
      <tr><td>Banner on BrimstokeBoxing.example</td><td>£2,000</td></tr>
      <tr><td>Press articles released daily in London, UK and sporting press</td><td>£5,000</td></tr>
      <tr><td>Signage and mentions throughout 2 hour live broadcast</td><td>£30,000</td></tr>
      <tr><td>Signage and mentions throughout re-runs</td><td>£15,000</td></tr>
      <tr><td>Broadcast of summarisation of events</td><td>£5,000</td></tr>
      <tr><td>Signage on post fight interviews</td><td>£5,000</td></tr>
      <tr><td>Public workout</td><td>£5,000</td></tr>
      <tr><td>Articles in press in all media</td><td>£5,000</td></tr>
      <tr><td>CRM &amp; video on ClipStream, VidRiver</td><td>£5,000</td></tr>
      <tr><td><b>Display advertising, value of all methods united</b></td><td>£92,000</td></tr>
    </table>
  </div>
  <div class="photo" style="left:0;top:300px;width:80px;height:68px;background:linear-gradient(#1b2233,#7a5a44)" role="img" aria-label="Boxers exchanging punches in the ring"></div>
  <div class="photo" style="left:81px;top:300px;width:80px;height:68px;background:linear-gradient(#2a2a2a,#a23a2c)" role="img" aria-label="Boxer landing a body shot"></div>
  <div class="photo" style="left:162px;top:300px;width:80px;height:68px;background:linear-gradient(#151d2c,#5b6f8c)" role="img" aria-label="Referee watching a close exchange"></div>
</section>

<!-- Packages -->
<section class="page pack-page">
  <div class="photo" style="left:0;top:0;width:100px;height:368px;background:linear-gradient(#1b1410,#7c2a22 45%,#1b1410)" role="img" aria-label="Boxer in red gloves with guard raised"></div>
  <div class="abs h" style="left:110px;top:14px;font-size:8px;color:var(--dark)">Sponsorship Packages</div>
  <div class="abs copy" style="left:110px;top:30px;width:122px">
    <div class="h" style="font-size:6px;color:var(--dark)">Amber package <span class="price">£60,000</span></div>
    Central branding signage on ringmatt. Signage on 2 cornerposts. Branding on one of the ring ropes. Signage in corners on ringmatt. Presence of logo on all media. Tickets per event: 15 front row ringside, 10 ringside, 50 unreserved seating. Hospitality VIP Access. Cocktail +25 VIP bracelets.<br><br>
    <div class="h" style="font-size:6px;color:var(--dark)">Silver package <span class="price">£35,000</span></div>
    Signage on 1 corner post. Signage on 'Wedgelet' cushions. Presence of logo at press conferences. Tickets per event: 8 front row, 4 ringside, 30 unreserved seating. Hospitality VIP Access. Cocktail +12 VIP bracelets.<br><br>
    <div class="h" style="font-size:6px;color:var(--dark)">Bronze package <span class="price">£20,000</span></div>
    Tickets per event: 4 front row ringside, 4 ringside enclosure, 20 unreserved seating. Cocktail &amp; 8 VIP bracelets.
  </div>
  <div class="photo" style="left:182px;top:318px;width:60px;height:50px;background:linear-gradient(225deg,#2b78b6,#15283f)" role="img" aria-label="Blue boxing glove"></div>
</section>

<!-- Back cover -->
<section class="page hands-page">
  <div class="photo" style="left:0;top:0;width:242px;height:368px;background:linear-gradient(#5a4030,#8a6446 40%,#1f2f6b 70%,#a3232b)" role="img" aria-label="Fighters' wrapped hands bumping fists over a union flag"></div>
</section>

</body>
</html>
```